New Corporate Business Card - Velmorana

What we need:
We need a new corporate business card.
We want a new template that we can change by ourself.
We want business card modern and minimalist but that looks professional.
We will print it in 300 gr soft-touch.
Why not a white side with the logo and a red/grey side with the content?
Why not a grey side and a red side like our logo?
I am sure that you have better idea than ours that's the reason we come here.

Who we are:
We are a private label company in cosmetics based in Switzerland. We work in BtoB. We make skin care products for other brands.

Target Market(s)

B to B - Worldwide - any gender

Industry/Entity Type

Cosmetics

Contact Information for Business Card

Side 1:
Logo
Your Swiss Private Label Manufacturer or www.velmorana-example.ch

Side 2:
Name and surname (Example: Lucien Marchetaz)
Job Description (General Manager)
Telephone (+41 32 915 63 00)
Direct (+41 32 915 63 63)
Email (lucien.marchetaz@velmorana-example.ch)
Chemin des Pélerines 14, 2000 Neuchâtel, Switzerland
www.velmorana-example.ch

Font styles to use
Serif
Sans Serif

Requirements
Must have
• You can use 4 colors: white, red, grey and/or black .
Should not have
• Too much colors, too much things. We want it simple!

```html
<!DOCTYPE html>
<html lang="en">
<head>
<meta charset="utf-8">
<title>Velmorana – Business Card</title>
<link rel="stylesheet" href="https://fonts.googleapis.com/css2?family=Hind:wght@300;400;600&display=swap">
<style>
  :root {
    --red: #ee3d48;
    --grey: #a9aaac;
    --white: #ffffff;
    --page: #ffffff;
  }
  * { box-sizing: border-box; margin: 0; padding: 0; }
  html, body { width: 1200px; height: 1200px; overflow: hidden; background: var(--page); }
  body { position: relative; font-family: "Hind", sans-serif; color: var(--white); }

  .card {
    position: absolute;
    left: 309px;
    width: 619px;
    overflow: hidden;
    box-shadow: 0 0 90px rgba(0, 0, 0, 0.035);
  }

  /* Front side */
  .card--front { top: 195px; height: 355px; background: var(--red); }
  .card--front .band-top {
    position: absolute; left: 0; top: 0; width: 100%; height: 175px;
    background: var(--grey);
    border-bottom: 3px solid var(--white);
  }
  .brand-block {
    position: absolute; left: 0; top: 0; width: 100%; height: 172px;
    display: flex; align-items: center; justify-content: center; gap: 18px;
  }
  .brand-mark { width: 26px; height: 26px; background: var(--white); flex: none; }
  .brand-name {
    font-weight: 300; font-size: 58px; letter-spacing: 4px; line-height: 1;
    padding-top: 8px;
  }
  .front-url {
    position: absolute; left: 0; width: 100%; top: 312px;
    text-align: center; font-weight: 300; font-size: 27px; letter-spacing: -0.3px;
  }

  /* Back side */
  .card--back { top: 582px; height: 354px; background: var(--grey); }
  .card--back .band-top {
    position: absolute; left: 0; top: 0; width: 100%; height: 180px;
    background: var(--red);
    border-bottom: 3px solid var(--white);
  }
  .back-brand {
    position: absolute; left: 40px; top: 27px; width: 200px; height: 116px;
    display: flex; align-items: center; gap: 10px;
  }
  .back-brand .brand-mark { width: 14px; height: 14px; }
  .back-brand .brand-name { font-size: 28px; letter-spacing: 2px; padding-top: 4px; }

  .person { position: absolute; right: 21px; top: 12px; text-align: right; }
  .person-name { font-weight: 600; font-size: 27px; line-height: 1.2; }
  .person-role { font-weight: 400; font-size: 13px; line-height: 1.2; }

  .contact-list {
    position: absolute; left: 21px; top: 230px; list-style: none;
  }
  .contact-item {
    display: flex; align-items: center; gap: 11px;
    height: 27px; font-weight: 300; font-size: 16px; white-space: nowrap;
  }
  .contact-icon { width: 18px; height: 18px; flex: none; }
</style>
</head>
<body>

<section class="card card--front" aria-label="Business card front">
  <div class="band-top"></div>
  <div class="brand-block">
    <span class="brand-mark"></span>
    <span class="brand-name">Velmorana</span>
  </div>
  <p class="front-url">www.velmorana-example.ch</p>
</section>

<section class="card card--back" aria-label="Business card back">
  <div class="band-top"></div>
  <div class="back-brand">
    <span class="brand-mark"></span>
    <span class="brand-name">Velmorana</span>
  </div>
  <div class="person">
    <p class="person-name">Lucien Marchetaz</p>
    <p class="person-role">General Manager</p>
  </div>

  <ul class="contact-list">
    <li class="contact-item">
      <svg class="contact-icon" viewBox="0 0 20 20" aria-hidden="true">
        <circle cx="10" cy="10" r="10" fill="#ee3d48"/>
        <path d="M6.5 5.2c.4-.3.9-.3 1.2.1l1.1 1.6c.2.4.2.8-.1 1.1l-.6.6c.5 1.1 1.3 1.9 2.4 2.4l.6-.6c.3-.3.8-.3 1.1-.1l1.6 1.1c.4.3.4.8.1 1.2l-.7.8c-.5.5-1.3.6-2 .3-2.2-1-3.9-2.7-4.9-4.9-.3-.7-.2-1.5.3-2z" fill="#fff"/>
      </svg>
      <span>+41 32 915 63 00</span>
    </li>
    <li class="contact-item">
      <svg class="contact-icon" viewBox="0 0 20 20" aria-hidden="true">
        <circle cx="10" cy="10" r="10" fill="#ee3d48"/>
        <path d="M6.5 5.2c.4-.3.9-.3 1.2.1l1.1 1.6c.2.4.2.8-.1 1.1l-.6.6c.5 1.1 1.3 1.9 2.4 2.4l.6-.6c.3-.3.8-.3 1.1-.1l1.6 1.1c.4.3.4.8.1 1.2l-.7.8c-.5.5-1.3.6-2 .3-2.2-1-3.9-2.7-4.9-4.9-.3-.7-.2-1.5.3-2z" fill="#fff"/>
      </svg>
      <span>+41 32 915 63 63</span>
    </li>
    <li class="contact-item">
      <svg class="contact-icon" viewBox="0 0 20 20" aria-hidden="true">
        <circle cx="10" cy="10" r="10" fill="#ee3d48"/>
        <rect x="5.5" y="7" width="9" height="6.5" rx="0.8" fill="none" stroke="#fff" stroke-width="1.2"/>
        <path d="M5.8 7.4 10 10.6l4.2-3.2" fill="none" stroke="#fff" stroke-width="1.2"/>
      </svg>
      <span>lucien.marchetaz@velmorana-example.ch</span>
    </li>
    <li class="contact-item">
      <svg class="contact-icon" viewBox="0 0 20 20" aria-hidden="true">
        <circle cx="10" cy="10" r="10" fill="#ee3d48"/>
        <path d="M10 4.5a3.6 3.6 0 0 0-3.6 3.6c0 2.7 3.6 6.9 3.6 6.9s3.6-4.2 3.6-6.9A3.6 3.6 0 0 0 10 4.5z" fill="#fff"/>
        <circle cx="10" cy="8.1" r="1.3" fill="#ee3d48"/>
      </svg>
      <span>Chemin des Pélerines 14, 2000 Neuchâtel, Switzerland</span>
    </li>
  </ul>
</section>

</body>
</html>
```